Letterhead and Envelope Design for Investment Company

We need a letterhead and envelope design.
We are a family owned investment company doing direct investments into other family owned businesses.
I have attached all our current marketing material including our logo for reference.

Our under construction website can be found here:
https://rob-darke-qv7m.pagevorlo.com/
password: Copperfen

Target Market(s)

Bankers, business owners, financial partners

Industry/Entity Type

Investment

Colors

Designer to choose colors to be used in the design.

Requirements
Must have
• Logo, and company information

```html
<!DOCTYPE html>
<html lang="en">
<head>
<meta charset="utf-8">
<title>Copperfen Holdings — Envelope</title>
<link href="https://fonts.googleapis.com/css2?family=Crimson+Pro:wght@400&display=swap" rel="stylesheet">
<style>
  :root {
    --backdrop: #e6e6e6;
    --paper: #2a272b;
    --paper-edge: #1f1d20;
    --gold: #b99528;
    --ink-light: #e9e6e1;
    --flap-line: #353236;
  }
  * { box-sizing: border-box; margin: 0; padding: 0; }
  html, body {
    width: 1200px; height: 900px; overflow: hidden;
    background: var(--backdrop);
  }
  .canvas {
    width: 1200px; height: 900px;
    display: flex; flex-direction: column;
    align-items: center; justify-content: center; gap: 60px;
  }
  .envelope {
    position: relative;
    width: 720px; height: 360px;
    background: var(--paper);
    font-family: "Crimson Pro", Georgia, serif;
  }
  /* Front */
  .sender {
    position: absolute; left: 40px; top: 34px;
    color: var(--ink-light);
  }
  .sender__name {
    font-size: 21px; letter-spacing: 0.06em;
    font-variant: small-caps;
    padding-bottom: 4px;
    border-bottom: 1px solid var(--gold);
  }
  .sender__suffix {
    font-size: 10px; letter-spacing: 0.12em;
    font-variant: small-caps;
    text-align: center; margin-top: 1px;
  }
  .sender__address {
    font-style: normal;
    font-size: 14px; line-height: 1.25;
    margin-top: 6px;
  }
  .contact-rule {
    position: absolute; left: 40px; right: 40px; bottom: 58px;
    border-top: 1px solid var(--gold);
  }
  .contact-line {
    position: absolute; left: 40px; bottom: 30px;
    color: var(--gold); font-size: 15px; letter-spacing: 0.01em;
  }
  /* Back */
  .envelope--back .flap {
    position: absolute; inset: 0; width: 100%; height: 100%;
  }
  .back-name {
    position: absolute; left: 0; right: 0; top: 168px;
    text-align: center;
    color: var(--gold);
    font-size: 20px; letter-spacing: 0.08em;
    font-variant: small-caps;
  }
</style>
</head>
<body>
<main class="canvas">
  <section class="envelope envelope--front" aria-label="Envelope front">
    <div class="sender">
      <div class="sender__name">Copperfen Holdings</div>
      <div class="sender__suffix">Inc.</div>
      <address class="sender__address">
        118 Marlow Ave. NE, Suite 210<br>
        Ashford Ridge, IA 52490
      </address>
    </div>
    <div class="contact-rule"></div>
    <p class="contact-line">555-204-7731 | inquiries@copperfenholdings.com | www.copperfenholdings.com</p>
  </section>

  <section class="envelope envelope--back" aria-label="Envelope back">
    <svg class="flap" viewBox="0 0 720 360" preserveAspectRatio="none" aria-hidden="true">
      <polyline points="6,8 360,140 714,8" fill="none" stroke="var(--flap-line)" stroke-width="1.5"/>
      <line x1="6" y1="8" x2="714" y2="8" stroke="var(--flap-line)" stroke-width="1"/>
    </svg>
    <div class="back-name">Copperfen Holdings</div>
  </section>
</main>
</body>
</html>
```